Tech Company requires UI design for mobile app

We need a mobile app design for a company based in Singapore called "Valdor Systems". We develop innovative Android/iOS business applications. KelmaRun - a collaboration tool targeted at SMEs that improves reporting and communication between different departments of an organisation. We would like to see designs that use the colour orange, our corporate colour. The final design should communicate clean and technology inclined design.

You are expected to recreate the icons, layout and structure without affecting the workflow.This is a workplace app for employee on mobile. The mobile app aims to empower individual employee to complete the following processes:

1. HR processes - taking attendance, timesheet, employment management to payslip)
2. Inventory management - stock taking, gift redemption and real-time stock management
3. Digital form - application for inspection, safety, procurement or request creation)
4. Job - an app that allows web portal to assign work to individual worker.
Updates

Project Deadline Extended
Reason: Received feedback to extens timeline. Cheers!

Target Market(s)

C-Executive, office employee, retail promoter, worker

Industry/Entity Type

Business

Colors

Designer to choose colors to be used in the design.

Requirements
Must have
• - Design must be neat, looks professional and perceived to be user-friendly
• - Use colour theme for each category
• - Must complement with KelmaRun logo them (already attached)
• - Have "apple" feel
• - We like the layout reference 1 & reference 2 photo. However, we prefer a better colour theme (Already Attached)
• - Please download the link for the work required
• https://files.quorvex.com/open?id=7Hq2LmPzXr4WtYb9NcKd3VfJsEa
Nice to have
• More info to follow shortly
Should not have
• - Must not be loud, flashy, dull, bored,
• - Design should not clash with Kelma Run Logo
• -

```html
<!DOCTYPE html>
<html lang="en">
<head>
<meta charset="utf-8">
<title>Valdor Workplace – Home</title>
<link href="https://fonts.googleapis.com/css2?family=Open+Sans:wght@400;600&display=swap" rel="stylesheet">
<style>
  :root{
    --page:#d6e3ef;
    --attendance:#7d88d8;
    --sales:#2aa6de;
    --inventory:#7fbf41;
    --leave:#ee6a32;
    --ink:#333a3f;
    --muted:#5e6469;
    --tab:#8a8f94;
    --rule:#dde2dd;
    --white:#ffffff;
  }
  *{box-sizing:border-box;margin:0;padding:0}
  html,body{width:1200px;height:1200px;overflow:hidden;background:var(--page);font-family:"Open Sans",Arial,sans-serif}
  .screen{
    position:absolute;left:50%;top:50%;width:552px;height:984px;
    margin:-492px 0 0 -276px;transform:scale(1.18);
    background:linear-gradient(180deg,#e3ece2 0%,#eef1ec 45%,#f4eeec 100%);
    overflow:hidden;box-shadow:0 10px 40px rgba(60,80,110,.18);
  }
  .hero{position:absolute;left:0;top:0;width:552px;height:280px;
    background:radial-gradient(ellipse at 50% 45%,#b7a493 0 18%,transparent 34%),linear-gradient(160deg,#6f8f4f 0%,#9ab97a 40%,#5e7b47 70%,#a8bf90 100%)}
  .wave{position:absolute;left:0;top:200px;width:552px;height:90px}
  .status{position:absolute;top:10px;left:0;width:100%;height:22px;color:var(--white);font-size:15px}
  .status .carrier{position:absolute;left:60px}
  .status .time{position:absolute;left:0;width:100%;text-align:center}
  .status .battery{position:absolute;right:12px;display:flex;align-items:center;gap:6px}
  .status .batt-body{width:30px;height:13px;border:1.5px solid var(--white);border-radius:3px;padding:1px}
  .status .batt-body span{display:block;height:100%;background:var(--white);border-radius:1px}
  .settings{position:absolute;left:467px;top:69px;width:52px;height:52px;border-radius:50%;background:rgba(255,255,255,.18);display:flex;align-items:center;justify-content:center}
  .profile{position:absolute;left:12px;top:288px}
  .profile h1{font-size:25px;font-weight:600;color:var(--ink);letter-spacing:.2px}
  .profile p{font-size:20px;color:var(--ink);margin-top:4px}
  .brand{position:absolute;right:16px;top:303px;display:flex;align-items:center;gap:8px;font-size:28px;color:var(--muted)}
  .brand i{width:14px;height:14px;border-radius:50%;background:var(--leave)}
  .section{position:absolute;left:12px;width:528px}
  .section h2{font-size:18px;font-weight:400;color:var(--ink);text-align:center;padding-bottom:8px;border-bottom:1px solid var(--rule)}
  .grid{display:flex;margin-top:13px}
  .item{width:132px;display:flex;flex-direction:column;align-items:center;text-align:center}
  .dot{width:56px;height:56px;border-radius:50%;display:flex;align-items:center;justify-content:center}
  .dot svg{width:26px;height:26px}
  .item span{font-size:13.5px;color:var(--muted);line-height:16px;margin-top:10px}
  .attendance .dot{background:var(--attendance)}
  .sales .dot{background:var(--sales)}
  .inventory .dot{background:var(--inventory)}
  .leave .dot{background:var(--leave)}
  .tabbar{position:absolute;left:0;top:907px;width:552px;height:77px;background:var(--white);display:flex}
  .tab{flex:1;display:flex;flex-direction:column;align-items:center;padding-top:10px;font-size:11px;color:var(--tab);position:relative}
  .tab svg{width:40px;height:38px}
  .tab.active{color:var(--leave);font-weight:600}
  .badge{position:absolute;top:10px;left:60px;width:20px;height:20px;border-radius:50%;background:#e8202a;color:var(--white);font-size:11px;display:flex;align-items:center;justify-content:center}
</style>
</head>
<body>
<main class="screen">
  <div class="hero" role="img" aria-label="Portrait photo of the employee outdoors among trees"></div>
  <svg class="wave" viewBox="0 0 552 90" preserveAspectRatio="none" aria-hidden="true">
    <path d="M0 40 C90 5 190 10 280 35 C370 60 460 20 552 30 L552 90 L0 90Z" fill="#e6eee5" opacity=".45"/>
    <path d="M0 70 C120 45 220 50 320 62 C420 72 490 55 552 62 L552 90 L0 90Z" fill="#e3ece2"/>
  </svg>
  <div class="status">
    <span class="carrier">NOVA</span>
    <span class="time">4:21 PM</span>
    <span class="battery">100% <span class="batt-body"><span></span></span></span>
  </div>
  <div class="settings"><svg width="26" height="26" viewBox="0 0 24 24"><path fill="#fff" d="M12 8.5a3.5 3.5 0 1 0 0 7 3.5 3.5 0 0 0 0-7zm9 5v-3l-2.3-.5-.7-1.6 1.3-2-2.1-2.1-2 1.3-1.6-.7L13 2h-3l-.5 2.3-1.6.7-2-1.3-2.1 2.1 1.3 2-.7 1.6L2 10.5v3l2.3.5.7 1.6-1.3 2 2.1 2.1 2-1.3 1.6.7.6 2.4h3l.5-2.3 1.6-.7 2 1.3 2.1-2.1-1.3-2 .7-1.6z"/></svg></div>

  <div class="profile"><h1>Mira Castell</h1><p>EM1104</p></div>
  <div class="brand"><i></i>Valdor</div>

  <section class="section attendance" style="top:382px">
    <h2>Attendance:</h2>
    <div class="grid">
      <div class="item"><div class="dot"><svg viewBox="0 0 24 24"><path fill="#fff" d="M12 2a7 7 0 0 0-7 7c0 5 7 13 7 13s7-8 7-13a7 7 0 0 0-7-7zm0 9.5A2.5 2.5 0 1 1 12 6.5a2.5 2.5 0 0 1 0 5z"/></svg></div><span>Take<br>Attendance</span></div>
      <div class="item"><div class="dot"><svg viewBox="0 0 24 24"><rect x="3" y="5" width="18" height="16" rx="2" fill="none" stroke="#fff" stroke-width="2"/><path stroke="#fff" stroke-width="2" d="M3 9h18M8 3v4M16 3v4"/><path fill="#fff" d="M7 12h2v2H7zm4 0h2v2h-2zm4 0h2v2h-2zM7 16h2v2H7zm4 0h2v2h-2zm4 0h2v2h-2z"/></svg></div><span>Today</span></div>
      <div class="item"><div class="dot"><svg viewBox="0 0 24 24"><rect x="5" y="4" width="14" height="18" rx="1.5" fill="none" stroke="#fff" stroke-width="2"/><rect x="9" y="2" width="6" height="4" rx="1" fill="#fff"/><path stroke="#fff" stroke-width="2" d="M8 11h8M8 15h8"/></svg></div><span>Past Records</span></div>
      <div class="item"><div class="dot"><svg viewBox="0 0 24 24"><circle cx="12" cy="8" r="3.2" fill="#fff"/><circle cx="5.5" cy="10" r="2.3" fill="#fff"/><circle cx="18.5" cy="10" r="2.3" fill="#fff"/><path fill="#fff" d="M6 19c0-3.5 2.7-6 6-6s6 2.5 6 6zM1 18c0-2.5 2-4.5 4.5-4.5 1 0 1.8.3 2.4.8C6.6 15.5 6 17 6 18zm22 0c0-2.5-2-4.5-4.5-4.5-1 0-1.8.3-2.4.8 1.3 1.2 1.9 2.7 1.9 3.7z"/></svg></div><span>Station</span></div>
    </div>
  </section>

  <section class="section sales" style="top:533px">
    <h2>Sales</h2>
    <div class="grid">
      <div class="item"><div class="dot"><svg viewBox="0 0 24 24"><rect x="3" y="8" width="18" height="4" fill="#fff"/><rect x="5" y="13" width="14" height="8" fill="#fff"/><path stroke="#2aa6de" stroke-width="2" d="M12 8v13"/><path fill="none" stroke="#fff" stroke-width="2" d="M12 8C10 3 6 4 7.5 7M12 8c2-5 6-4 4.5-1"/></svg></div><span>New<br>Redemption</span></div>
      <div class="item"><div class="dot"><svg viewBox="0 0 24 24"><path fill="#fff" d="M12 5C6 5 2 12 2 12s4 7 10 7 10-7 10-7-4-7-10-7zm0 11a4 4 0 1 1 0-8 4 4 0 0 1 0 8z"/><circle cx="12" cy="12" r="2" fill="#fff"/></svg></div><span>View<br>Redemptions</span></div>
      <div class="item"><div class="dot"><svg viewBox="0 0 24 24"><path fill="#fff" d="M8.5 4h7l1.5 2.5H21v13H3v-13h4zM12 9a4 4 0 1 0 0 8 4 4 0 0 0 0-8z"/><circle cx="12" cy="13" r="2.2" fill="#fff"/></svg></div><span>Take Photo</span></div>
      <div class="item"><div class="dot"><svg viewBox="0 0 24 24"><path fill="#fff" d="M4 14h3v7H4zm5-3h3v10H9zm5 2h3v8h-3zm5-5h3v13h-3z"/><path fill="none" stroke="#fff" stroke-width="2" d="M3 11l6-5 5 3 6-6"/></svg></div><span>Sales Summary</span></div>
    </div>
  </section>

  <section class="section inventory" style="top:684px">
    <h2>Inventory</h2>
    <div class="grid">
      <div class="item"><div class="dot"><svg viewBox="0 0 24 24"><path fill="none" stroke="#fff" stroke-width="2" d="M5 3h12v11M5 3v18h8M8 8h6M8 12h6M8 16h3"/><path fill="none" stroke="#fff" stroke-width="2" d="M14 18l2 2 4-4"/></svg></div><span>Inventory Check</span></div>
      <div class="item"><div class="dot"><svg viewBox="0 0 24 24"><path fill="#fff" d="M12 2l9 4.5-9 4.5-9-4.5zM3 8l8 4v10l-8-4zm18 0v10l-8 4V12z"/></svg></div><span>Delivery</span></div>
      <div class="item"><div class="dot"><svg viewBox="0 0 24 24"><path fill="#fff" d="M3 3h9l9 9-9 9-9-9zm4 2.5A1.5 1.5 0 1 0 7 8.5 1.5 1.5 0 0 0 7 5.5z"/></svg></div><span>New Stock Take</span></div>
      <div class="item"><div class="dot"><svg viewBox="0 0 24 24"><path fill="none" stroke="#fff" stroke-width="2" d="M8 3h10v8M8 3L4 7v14h9M4 7h4V3M7 12h7M7 16h4"/><path fill="#fff" d="M19 13l2 2-5 5h-2v-2z"/></svg></div><span>Stock Tack List</span></div>
    </div>
  </section>

  <section class="section leave" style="top:835px">
    <h2>Leave</h2>
    <div class="grid">
      <div class="item"><div class="dot"></div></div>
      <div class="item"><div class="dot"></div></div>
      <div class="item"><div class="dot"></div></div>
      <div class="item"><div class="dot"></div></div>
    </div>
  </section>

  <nav class="tabbar">
    <div class="tab active"><svg viewBox="0 0 40 38"><path fill="#ee6a32" d="M20 3L2 19h5v16h10V25h6v10h10V19h5z"/></svg>HOME</div>
    <div class="tab"><svg viewBox="0 0 40 38"><rect x="5" y="6" width="30" height="29" rx="3" fill="none" stroke="#9a9fa4" stroke-width="3"/><path stroke="#9a9fa4" stroke-width="3" d="M5 13h30M12 2v8M28 2v8"/><path fill="#9a9fa4" d="M10 18h4v4h-4zm8 0h4v4h-4zm8 0h4v4h-4zM10 26h4v4h-4zm8 0h4v4h-4zm8 0h4v4h-4z"/></svg>CALENDAR</div>
    <div class="tab"><svg viewBox="0 0 40 38"><path fill="#9a9fa4" d="M20 3c-6 0-10 4-10 10v10l-4 5v2h28v-2l-4-5V13c0-6-4-10-10-10zm-4 29a4 4 0 0 0 8 0z"/></svg>NOTIFICATION</div>
    <div class="tab"><svg viewBox="0 0 40 38"><path fill="none" stroke="#9a9fa4" stroke-width="3" d="M28 12a10 10 0 0 0-17 3M12 26a10 10 0 0 0 17-3"/><path fill="#9a9fa4" d="M25 6l6 1-1 6zM15 32l-6-1 1-6z"/></svg>SYNC<span class="badge">3</span></div>
    <div class="tab"><svg viewBox="0 0 40 38"><circle cx="20" cy="11" r="8" fill="#9a9fa4"/><path fill="#9a9fa4" d="M6 36c0-9 6-15 14-15s14 6 14 15z"/></svg>PROFILE</div>
  </nav>
</main>
</body>
</html>
```